Brightpath - online education agent and consultancy

Online education provider for business to business market needs a dynamic, modern and mobile friendly website. We have the shell view www.quorvane.example but it is boring!
I will need to add courses to the website - Business, Health and Wellbeing, Digital, Aviation.
I am targeting mainly services based industries - so blue collar workers, living in the outer suburbs, will be studying online and most likely from home.
They need to feel safe and secure - we are reputable and importantly can support them all the way to course completion.
What makes us stand out from everyone else - we dont offer any courses - we pick and choose the best courses, with the best providers and only offer quality.
We take the time to find out what the student really wants to achieve and match them with the right education provider.

Target Market(s)

Business to Business - HR managers, People and Culture Managers, employees who are 25+ years currently working wanting to further their careers with accredited qualifications

Industry/Entity Type

Education

Number of Pages Required

5+ page

Font styles to use
Sans Serif

Colors
00a990
acd036
0792cd
a54499
f37122

Requirements
Must have
• Mobile functionality - view on iphone/ipad
• Home page
• Courses section
• Contact us
• Payment checkout to be added
Nice to have
• Fresh, inviting, images that reflect the difference we will make - supporting people through the whole journey.
• It needs to be inviting - homely but modern
Should not have
• Black, dark colours

```html
<!DOCTYPE html>
<html lang="en">
<head>
<meta charset="utf-8">
<title>Quorvane – Courses</title>
<link rel="stylesheet" href="https://fonts.googleapis.com/css2?family=Raleway:wght@300;400;500;600&family=Open+Sans:wght@400&display=swap">
<style>
  :root {
    --white: #ffffff;
    --ink: #333333;
    --text: #4a4a4a;
    --green-light: #b4d94a;
    --green: #9cc93a;
    --green-deep: #4e9a14;
    --green-brand: #7fbf2a;
    --orange: #f37122;
    --blue: #1a7ec4;
    --rule: #d6d6d6;
  }
  * { box-sizing: border-box; margin: 0; padding: 0; }
  html, body { width: 1200px; height: 1019px; overflow: hidden; background: var(--white); }
  body { position: relative; font-family: "Open Sans", sans-serif; color: var(--text); }

  .site-header { position: absolute; left: 0; top: 0; width: 1200px; height: 128px; }
  .brand { position: absolute; left: 0; width: 1200px; top: 52px; text-align: center;
    font-family: "Raleway", sans-serif; font-weight: 300; font-size: 52px; letter-spacing: 6px;
    color: var(--green-brand); line-height: 1; }
  .phone { position: absolute; left: 910px; top: 80px; display: flex; align-items: center; gap: 6px;
    font-family: "Raleway", sans-serif; font-weight: 600; font-size: 21px; color: var(--ink); line-height: 30px; }
  .phone-icon { width: 30px; height: 30px; flex: none; }

  .main-nav { position: absolute; left: 0; top: 128px; width: 1200px; height: 58px;
    background: linear-gradient(var(--green-light), var(--green)); display: flex; justify-content: center; }
  .main-nav a { display: flex; align-items: center; justify-content: center; height: 58px;
    color: var(--white); text-decoration: none; font-family: "Raleway", sans-serif; font-weight: 500;
    font-size: 18px; border-left: 1px solid rgba(255,255,255,.35); }
  .main-nav a:first-child { border-left: none; }
  .main-nav .active { background: linear-gradient(var(--green), var(--green-deep)); }

  .hero { position: absolute; left: 0; top: 186px; width: 1200px; height: 298px;
    background:
      radial-gradient(ellipse 140px 170px at 230px 150px, rgba(214,168,140,.75), transparent),
      radial-gradient(ellipse 130px 170px at 450px 150px, rgba(224,182,160,.75), transparent),
      radial-gradient(ellipse 130px 170px at 740px 170px, rgba(160,110,80,.7), transparent),
      radial-gradient(ellipse 150px 190px at 900px 160px, rgba(200,130,90,.75), transparent),
      linear-gradient(180deg, rgba(255,255,255,0) 55%, rgba(80,70,110,.25) 100%),
      linear-gradient(90deg, #d8d6d0 0%, #8a7fa0 18%, #b89684 30%, #c49a72 42%, #7b6a56 55%, #a78a70 68%, #c08a72 80%, #dedcd6 100%);
    border-bottom: 2px solid var(--rule); }

  .intro { position: absolute; left: 145px; top: 550px; width: 540px; }
  .intro h1 { font-family: "Raleway", sans-serif; font-weight: 400; font-size: 31px; color: var(--ink);
    margin-bottom: 17px; letter-spacing: .3px; line-height: 36px; }
  .intro p { font-size: 13px; line-height: 18px; margin-bottom: 17px; }

  .course-visual { position: absolute; left: 714px; top: 573px; width: 351px; height: 232px;
    background:
      radial-gradient(ellipse 120px 60px at 160px 70px, rgba(110,100,170,.35), transparent),
      radial-gradient(ellipse 150px 60px at 200px 190px, rgba(255,255,255,.95), transparent),
      linear-gradient(#dcdce2, #eeeef0 45%, #f6f5f2 70%, #bdb7ae 100%); }

  .site-footer { position: absolute; left: 0; top: 899px; width: 1200px; height: 120px; background: var(--blue); }
  .footer-nav { position: absolute; left: 127px; top: 33px; display: flex; gap: 40px; }
  .footer-nav a { color: var(--white); text-decoration: none; font-family: "Raleway", sans-serif;
    font-weight: 500; font-size: 15.5px; }
  .legal { position: absolute; left: 127px; top: 65px; color: var(--white); font-size: 12.5px; }
  .social { position: absolute; left: 934px; top: 37px; display: flex; gap: 10px; }
  .social a { display: block; width: 24px; height: 24px; border-radius: 50%;
    border: 2px solid var(--white); background: rgba(255,255,255,.18); }
</style>
</head>
<body>
  <header class="site-header">
    <div class="brand">QUORVANE</div>
    <div class="phone">
      <svg class="phone-icon" viewBox="0 0 30 30" aria-hidden="true">
        <circle cx="15" cy="15" r="15" fill="#f37122"/>
        <path d="M10 8c1-1 2-1 3 0l2 3c.5 1 0 2-1 2.5 1 2 2 3 4 4 .5-1 1.5-1.5 2.5-1l3 2c1 1 1 2 0 3-2 2-5 1.5-8-1.5S8 10 10 8z" fill="none" stroke="#fff" stroke-width="1.6"/>
      </svg>
      1300 55 01 99
    </div>
  </header>

  <nav class="main-nav">
    <a href="#" style="width:110px">HOME</a>
    <a href="#" style="width:200px">BRIGHTPATH</a>
    <a href="#" class="active" style="width:193px">OUR COURSES</a>
    <a href="#" style="width:167px">LET'S CHAT</a>
    <a href="#" style="width:200px">ABOUT QUORVANE</a>
  </nav>

  <div class="hero" role="img" aria-label="Photo of smiling students gathered around a laptop"></div>

  <main class="intro">
    <h1>COURSES</h1>
    <p>We offer accredited educational courses from a range of institutions that we know deliver the best of blended learning in their field.</p>
    <p>We aren't a one size fits all.</p>
    <p>At QUORVANE we take the time to understand what you want to achieve from study and match you with the right education provider and course.</p>
    <p>We work with Universities, TAFE and Private Education Colleges. From Certificate III, Certificate IV, Diplomas and even MBA's we can advise you on the best fit course for you.</p>
  </main>

  <div class="course-visual" role="img" aria-label="Illustration of an open book with letters flying out of it"></div>

  <footer class="site-footer">
    <nav class="footer-nav">
      <a href="#">HOME</a>
      <a href="#">BRIGHTPATH</a>
      <a href="#">OUR COURSES</a>
      <a href="#">LET'S CHAT</a>
      <a href="#">ABOUT QUORVANE</a>
    </nav>
    <p class="legal">© 2016 Company Name &nbsp;All right reserved &nbsp;Term of Use</p>
    <div class="social" aria-label="Social links"><a href="#" aria-label="Social link 1"></a><a href="#" aria-label="Social link 2"></a><a href="#" aria-label="Social link 3"></a><a href="#" aria-label="Social link 4"></a></div>
  </footer>
</body>
</html>
```